WardPivot landing page

The existing website at www.wardpivot-example.com needs updating. I've attached some marketing material for the color scheme to be used and potential content. The tagline should be "Real-Time Operational Intelligence." I want the landing page to be in 3 categories in this order and features within each category. Plenty of images are preferred and wording can be modified.
Wardpivot Command Centre
- Live Incident tracking and reporting with escalation on critical incidents if necessary
- Geofence Monitoring to ensure guards at the right location at the right time.
- Smart scheduling to ensure the correct training and certifications are assigned to the appropriate guard required.
- Camera compatibility to capture live and historical video for incident reporting
WardPivot Back Office Administration
- Automate Police report filing using data from submitted incidents when required.
- Track all required KPIs on a per site basis such as vehicle inspections, patrol tour details, etc
- Payroll and Invoicing using smart shift reports
- Create and manage client sites with configurable geofencing
WardPivot App
- Guard can see all site details and instructions when logging onto shift
- Ability to view all incidents that have occured at that particular site over the last 'x' days. Understand what has been happening and when.
- Report incidents with all relevant information including photo and video
- Recieve alerts when repeat offences are occuring within a configurable vicinity.

Target Market(s)

Retailers and guard companies

Coding

Coded - Design and coding required

Number of Pages Required

1 page

Requirements
Nice to have
• Use the look and feel of the logo in the design

```html
<!DOCTYPE html>
<html lang="en">
<head>
<meta charset="utf-8">
<title>WardPivot — Real-Time Operational Intelligence</title>
<link href="https://fonts.googleapis.com/css2?family=Barlow+Condensed:wght@600;700&family=Inter:wght@400;500;600;700&display=swap" rel="stylesheet">
<style>
:root{
  --blue:#1a8fd6;
  --navy:#0f2547;
  --navy-2:#1b3560;
  --ink:#0d1b33;
  --grey:#9aa3ae;
  --text:#3a4250;
  --light:#f1f3f6;
  --white:#ffffff;
}
*{margin:0;padding:0;box-sizing:border-box}
html,body{width:1200px;height:3386px;overflow:hidden}
body{font-family:"Inter",sans-serif;color:var(--ink);background:var(--white);position:relative}
section,header,footer{position:relative;width:1200px}
.abs{position:absolute}
.heading{font-family:"Barlow Condensed",sans-serif;font-weight:700;line-height:1.05;color:var(--ink)}
.media{position:absolute}
.btn{position:absolute;display:flex;align-items:center;justify-content:center;font-family:"Barlow Condensed",sans-serif;font-weight:700;font-size:13px;letter-spacing:.3px;text-transform:uppercase}
.btn-blue{background:var(--blue);color:var(--white)}
.btn-white{background:var(--white);color:var(--ink)}
.brand{font-family:"Inter",sans-serif;font-weight:700;color:var(--navy);display:flex;align-items:center;gap:8px}
.brand-mark{display:inline-block;background:var(--blue)}

/* hero */
.hero{height:627px;background:linear-gradient(110deg,#e4ecf4 0%,#f2f4f7 45%,#eef1f5 100%)}
.nav-links{position:absolute;left:640px;top:47px;display:flex;gap:37px;font-size:11px;color:var(--ink)}
.nav-links .active::before{content:"";display:inline-block;width:5px;height:5px;background:var(--blue);margin-right:5px;vertical-align:middle}
.hero-kicker{left:125px;top:224px;font-size:38px;color:var(--blue)}
.hero-title{left:125px;top:262px;font-size:66px}
.hero-sub{left:125px;top:336px;width:360px;font-size:15px;font-weight:600;letter-spacing:-.3px;line-height:1.25}
.hero-desc{left:125px;top:386px;width:400px;font-size:10.5px;color:var(--text);line-height:1.45}

/* photo areas */
.photo-hero{background:
  radial-gradient(ellipse 40% 35% at 42% 40%,rgba(70,170,235,.55),transparent 70%),
  radial-gradient(ellipse 30% 60% at 82% 55%,rgba(8,12,20,.9),transparent 70%),
  radial-gradient(ellipse 60% 25% at 45% 85%,rgba(40,110,170,.45),transparent 70%),
  linear-gradient(160deg,#0a1626,#15395c 45%,#0b1a2c)}
.photo-command{background:
  radial-gradient(ellipse 30% 30% at 38% 35%,rgba(60,200,180,.5),transparent 70%),
  radial-gradient(ellipse 25% 25% at 28% 72%,rgba(60,200,170,.4),transparent 70%),
  radial-gradient(ellipse 35% 30% at 78% 45%,rgba(120,170,200,.35),transparent 70%),
  linear-gradient(135deg,#06121f,#0c2d3e 50%,#0a2236 80%,#061220)}
.photo-office{background:
  radial-gradient(ellipse 45% 22% at 48% 38%,rgba(255,255,255,.95),transparent 70%),
  radial-gradient(ellipse 50% 25% at 50% 88%,rgba(40,44,50,.55),transparent 70%),
  linear-gradient(180deg,#e3e6ea,#d2d6db 55%,#b7bcc3)}
.photo-app{background:
  radial-gradient(ellipse 12% 18% at 25% 55%,rgba(225,240,255,.7),transparent 70%),
  radial-gradient(ellipse 30% 45% at 70% 60%,rgba(20,35,70,.9),transparent 70%),
  radial-gradient(ellipse 40% 30% at 35% 20%,rgba(150,140,120,.35),transparent 70%),
  linear-gradient(135deg,#3a3f47,#1d2b45 50%,#0d1628)}
.photo-team{background:
  radial-gradient(ellipse 35% 30% at 30% 30%,rgba(90,190,240,.45),transparent 70%),
  radial-gradient(ellipse 35% 35% at 65% 55%,rgba(30,60,90,.7),transparent 70%),
  radial-gradient(ellipse 45% 25% at 50% 90%,rgba(5,12,22,.8),transparent 70%),
  linear-gradient(135deg,#12304c,#1d4f73 50%,#0a1b2e)}

/* trust */
.trust{height:376px;background:var(--white)}
.trust-title{left:351px;top:110px;font-size:40px;width:560px}
.trust-title .muted{color:var(--grey)}

/* feature blocks */
.feature-title{font-size:39px}
.feature-desc{font-size:9.8px;line-height:1.55;color:var(--text);width:395px}
.accordion{position:absolute;width:387px;padding:12px 21px 14px}
.acc-item{display:flex;align-items:center;height:30px;font-size:13px;font-weight:500;letter-spacing:-.2px}
.acc-item .label{flex:1}
.tick{width:15px;height:15px;background:var(--blue);border-radius:2px;margin-right:11px;display:flex;align-items:center;justify-content:center}
.chev{width:15px;height:15px;background:var(--navy);border-radius:2px;display:flex;align-items:center;justify-content:center}
.acc-points{list-style:none;margin:-2px 0 4px 26px}
.acc-points li{font-size:9px;color:var(--text);line-height:18px}
.acc-points li::before{content:"";display:inline-block;width:4px;height:4px;background:var(--blue);margin-right:5px;vertical-align:middle}

.command{height:522px;background:var(--light)}
.command .accordion{background:var(--white)}
.office{height:538px;background:var(--white)}
.office .accordion{background:var(--light)}
.app{height:553px;background:var(--navy)}
.app .heading,.app .feature-desc{color:var(--white)}
.app .accordion{background:var(--navy-2);color:var(--white)}
.app .acc-points li{color:#d5deea}
.app .chev{background:#3d5479}

/* cta */
.cta{height:343px;background:var(--blue)}
.cta-title{left:690px;top:66px;font-size:40px;color:var(--white);width:360px}
.cta-desc{left:690px;top:200px;width:380px;font-size:10px;color:var(--white);line-height:1.5}

/* footer */
.site-footer{height:427px;background:linear-gradient(180deg,#eef1f5,#f4f5f7)}
.footer-text{left:412px;top:222px;width:376px;text-align:center;font-size:10.5px;color:var(--text);line-height:1.5}
.socials{left:549px;top:274px;display:flex;gap:10px}
.socials span{width:27px;height:27px;background:var(--blue);display:block}
.footer-rule{left:125px;top:383px;width:950px;height:1px;background:#d7dbe1}
.footer-small{top:396px;font-size:9.5px;color:var(--text)}
</style>
</head>
<body>

<header class="hero">
  <div class="brand abs" style="left:125px;top:44px;font-size:22px"><span class="brand-mark" style="width:22px;height:22px"></span>WardPivot</div>
  <nav class="nav-links">
    <span class="active">Home</span><span>Features</span><span>Pricing</span><span>Contact Us</span>
  </nav>
  <div class="btn btn-blue" style="left:979px;top:37px;width:96px;height:33px">
    <svg width="10" height="10" viewBox="0 0 10 10" style="margin-right:5px"><circle cx="5" cy="3" r="2" fill="none" stroke="#fff"/><path d="M1 10c0-3 8-3 8 0" fill="none" stroke="#fff"/></svg>Login
  </div>
  <div class="heading abs hero-kicker">Real-Time Operational</div>
  <h1 class="heading abs hero-title">Intelligence</h1>
  <p class="abs hero-sub">Manage your entire security workforce within one secure platform</p>
  <p class="abs hero-desc">Streamline operations, enhance security, and ensure compliance with WardPivot's integrated management solution.</p>
  <div class="btn btn-blue" style="left:125px;top:431px;width:141px;height:33px">Request a Demo</div>
  <div class="media photo-hero" role="img" aria-label="Security supervisor pointing at a wall of live monitoring screens in a dark control room" style="left:622px;top:125px;width:453px;height:443px"></div>
</header>

<section class="trust">
  <div class="abs" style="left:125px;top:90px;width:190px;display:flex;flex-direction:column;align-items:center;gap:14px">
    <span class="brand-mark" style="width:130px;height:130px"></span>
    <span class="brand" style="font-size:26px">WardPivot</span>
  </div>
  <h2 class="heading abs trust-title">Trusted By Security Teams To Deliver Real-Time Visibility, <span class="muted">Compliance, And Accountability.</span></h2>
</section>

<section class="command">
  <h2 class="heading abs feature-title" style="left:125px;top:100px">WardPivot Command Centre</h2>
  <p class="abs feature-desc" style="left:125px;top:151px">Centralized Command. Immediate Insight. Description: The WardPivot Command Centre provides live visibility into every incident, guard movement, and site condition empowering supervisors to act decisively.</p>
  <div class="accordion" style="left:125px;top:213px">
    <div class="acc-item"><span class="tick"><svg width="9" height="9" viewBox="0 0 9 9"><path d="M1 4.5l2.5 2.5L8 2" fill="none" stroke="#fff" stroke-width="1.6"/></svg></span><span class="label">Live Incident Tracking &amp; Escalation</span><span class="chev"><svg width="8" height="8" viewBox="0 0 8 8"><path d="M1 5.5l3-3 3 3" fill="none" stroke="#fff" stroke-width="1.4"/></svg></span></div>
    <ul class="acc-points"><li>Real-time incident tracking with detailed reporting</li><li>Automated escalation workflows for critical incidents</li><li>Supervisor visibility across all active sites</li></ul>
    <div class="acc-item"><span class="tick"><svg width="9" height="9" viewBox="0 0 9 9"><path d="M1 4.5l2.5 2.5L8 2" fill="none" stroke="#fff" stroke-width="1.6"/></svg></span><span class="label">Geofence Monitoring</span><span class="chev"><svg width="8" height="8" viewBox="0 0 8 8"><path d="M1 2.5l3 3 3-3" fill="none" stroke="#fff" stroke-width="1.4"/></svg></span></div>
    <div class="acc-item"><span class="tick"><svg width="9" height="9" viewBox="0 0 9 9"><path d="M1 4.5l2.5 2.5L8 2" fill="none" stroke="#fff" stroke-width="1.6"/></svg></span><span class="label">Smart Scheduling &amp; Certifications</span><span class="chev"><svg width="8" height="8" viewBox="0 0 8 8"><path d="M1 2.5l3 3 3-3" fill="none" stroke="#fff" stroke-width="1.4"/></svg></span></div>
    <div class="acc-item"><span class="tick"><svg width="9" height="9" viewBox="0 0 9 9"><path d="M1 4.5l2.5 2.5L8 2" fill="none" stroke="#fff" stroke-width="1.6"/></svg></span><span class="label">Camera Compatibility</span><span class="chev"><svg width="8" height="8" viewBox="0 0 8 8"><path d="M1 2.5l3 3 3-3" fill="none" stroke="#fff" stroke-width="1.4"/></svg></span></div>
  </div>
  <div class="media photo-command" role="img" aria-label="Command centre video wall showing site maps and live camera feeds" style="left:599px;top:80px;width:476px;height:363px"></div>
</section>

<section class="office">
  <div class="media photo-office" role="img" aria-label="Office desk with two monitors showing analytics dashboards and payroll screens" style="left:125px;top:87px;width:474px;height:362px"></div>
  <h2 class="heading abs feature-title" style="left:650px;top:90px;width:400px">WardPivot Back Office Administration</h2>
  <p class="abs feature-desc" style="left:650px;top:180px;width:390px">Automate Administration. Gain Total Oversight. Description: WardPivot's back office tools reduce paperwork, improve accuracy, and provide actionable insights across every client site.</p>
  <div class="accordion" style="left:650px;top:240px">
    <div class="acc-item"><span class="tick"><svg width="9" height="9" viewBox="0 0 9 9"><path d="M1 4.5l2.5 2.5L8 2" fill="none" stroke="#fff" stroke-width="1.6"/></svg></span><span class="label">Automated Police Report Filing</span><span class="chev"><svg width="8" height="8" viewBox="0 0 8 8"><path d="M1 5.5l3-3 3 3" fill="none" stroke="#fff" stroke-width="1.4"/></svg></span></div>
    <ul class="acc-points"><li>Generate police reports directly from incident data</li><li>Reduce manual data entry and reporting delays</li><li>Ensure accuracy and consistency</li></ul>
    <div class="acc-item"><span class="tick"><svg width="9" height="9" viewBox="0 0 9 9"><path d="M1 4.5l2.5 2.5L8 2" fill="none" stroke="#fff" stroke-width="1.6"/></svg></span><span class="label">KPI Tracking By Site</span><span class="chev"><svg width="8" height="8" viewBox="0 0 8 8"><path d="M1 2.5l3 3 3-3" fill="none" stroke="#fff" stroke-width="1.4"/></svg></span></div>
    <div class="acc-item"><span class="tick"><svg width="9" height="9" viewBox="0 0 9 9"><path d="M1 4.5l2.5 2.5L8 2" fill="none" stroke="#fff" stroke-width="1.6"/></svg></span><span class="label">Payroll &amp; Invoicing</span><span class="chev"><svg width="8" height="8" viewBox="0 0 8 8"><path d="M1 2.5l3 3 3-3" fill="none" stroke="#fff" stroke-width="1.4"/></svg></span></div>
    <div class="acc-item"><span class="tick"><svg width="9" height="9" viewBox="0 0 9 9"><path d="M1 4.5l2.5 2.5L8 2" fill="none" stroke="#fff" stroke-width="1.6"/></svg></span><span class="label">Site &amp; Geofence Management</span><span class="chev"><svg width="8" height="8" viewBox="0 0 8 8"><path d="M1 2.5l3 3 3-3" fill="none" stroke="#fff" stroke-width="1.4"/></svg></span></div>
  </div>
</section>

<section class="app">
  <h2 class="heading abs feature-title" style="left:125px;top:123px">WardPivot App</h2>
  <p class="abs feature-desc" style="left:125px;top:174px">Everything Guards Need, Right in Their Hands. Description: The WardPivot mobile app ensures guards are informed, connected, and equipped to respond effectively.</p>
  <div class="accordion" style="left:125px;top:221px">
    <div class="acc-item"><span class="tick"><svg width="9" height="9" viewBox="0 0 9 9"><path d="M1 4.5l2.5 2.5L8 2" fill="none" stroke="#fff" stroke-width="1.6"/></svg></span><span class="label">Site Details &amp; Shift Instructions</span><span class="chev"><svg width="8" height="8" viewBox="0 0 8 8"><path d="M1 5.5l3-3 3 3" fill="none" stroke="#fff" stroke-width="1.4"/></svg></span></div>
    <ul class="acc-points"><li>Guards view site instructions upon logging into a shift</li><li>Clear expectations and procedures</li><li>Reduced onboarding and training friction</li></ul>
    <div class="acc-item"><span class="tick"><svg width="9" height="9" viewBox="0 0 9 9"><path d="M1 4.5l2.5 2.5L8 2" fill="none" stroke="#fff" stroke-width="1.6"/></svg></span><span class="label">Incident History Visibility</span><span class="chev"><svg width="8" height="8" viewBox="0 0 8 8"><path d="M1 2.5l3 3 3-3" fill="none" stroke="#fff" stroke-width="1.4"/></svg></span></div>
    <div class="acc-item"><span class="tick"><svg width="9" height="9" viewBox="0 0 9 9"><path d="M1 4.5l2.5 2.5L8 2" fill="none" stroke="#fff" stroke-width="1.6"/></svg></span><span class="label">Incident Reporting With Media</span><span class="chev"><svg width="8" height="8" viewBox="0 0 8 8"><path d="M1 2.5l3 3 3-3" fill="none" stroke="#fff" stroke-width="1.4"/></svg></span></div>
    <div class="acc-item"><span class="tick"><svg width="9" height="9" viewBox="0 0 9 9"><path d="M1 4.5l2.5 2.5L8 2" fill="none" stroke="#fff" stroke-width="1.6"/></svg></span><span class="label">Repeat Offence Alerts</span><span class="chev"><svg width="8" height="8" viewBox="0 0 8 8"><path d="M1 2.5l3 3 3-3" fill="none" stroke="#fff" stroke-width="1.4"/></svg></span></div>
  </div>
  <div class="media photo-app" role="img" aria-label="Uniformed guard using the mobile app on a phone at night in the city" style="left:644px;top:82px;width:474px;height:391px"></div>
</section>

<section class="cta">
  <div class="media photo-team" role="img" aria-label="Operators working at holographic monitoring screens in an operations centre" style="left:0;top:0;width:600px;height:343px"></div>
  <h2 class="heading abs cta-title">See Real-Time Operational Intelligence In Action</h2>
  <p class="abs cta-desc">Discover how WardPivot transforms security operations from the field to the command center.</p>
  <div class="btn btn-white" style="left:690px;top:241px;width:141px;height:32px">Request a Demo</div>
</section>

<footer class="site-footer">
  <div class="abs" style="left:500px;top:68px;width:200px;display:flex;flex-direction:column;align-items:center;gap:16px">
    <span class="brand-mark" style="width:70px;height:70px"></span>
    <span class="brand" style="font-size:32px">WardPivot</span>
  </div>
  <p class="abs footer-text">Real-time operational intelligence for modern security operations. Empowering security teams with visibility, control, and accountability.</p>
  <div class="abs socials"><span></span><span></span><span></span></div>
  <div class="abs footer-rule"></div>
  <div class="abs footer-small" style="left:125px">© 2026 WardPivot. All rights reserved.</div>
  <div class="abs footer-small" style="right:125px">Privacy Policy | Terms of Service</div>
</footer>

</body>
</html>
```